Marta Business Card

My wife is going to start her own business with renting holiday appartments to tourists. She needs a design for a new business card... and a new web site.
Look at Stayvolt "Erholung auf dem Lindenwäldchen"

Target Market(s)

Give business card to prospects at any situation

Contact Information for Business Card

not sure what this means

Font styles to use
Script

Colors
fec41a
fee18a

Requirements
Must have
• My wife's handwriting is difficult to read:
Entspannen - Loslassen - Auftanken
Marta & das Lindenwäldchen
Urlaub an einem besonderen Ort
Marta Brecke
Grauer Pfad 7
18471 Alt Feldow
post@marta-brecke.de
www.lindenwaeldchen.net
Nice to have
• Beige background
Font like handwriting

```html
<!DOCTYPE html>
<html lang="de">
<head>
<meta charset="utf-8">
<title>Marta &amp; das Lindenwäldchen – Visitenkarte</title>
<link rel="stylesheet" href="https://fonts.googleapis.com/css2?family=Montserrat:wght@400;500;700&family=Playball&display=swap">
<style>
  :root {
    --page: #ffffff;
    --paper: #ece4da;
    --paper-light: #f3ede5;
    --wine: #6e0d0d;
    --ink: #1e1a1a;
    --black: #0c0b0b;
    --white: #ffffff;
    --script: "Playball", cursive;
    --sans: "Montserrat", sans-serif;
  }
  * { margin: 0; padding: 0; box-sizing: border-box; }
  html, body {
    width: 740px; height: 1200px; overflow: hidden;
    background: var(--page);
  }
  .card {
    position: absolute; left: 60px;
    width: 620px; height: 356px;
    background: linear-gradient(135deg, var(--paper-light), var(--paper));
    box-shadow: 2px 3px 6px rgba(0,0,0,.25);
    overflow: hidden;
  }
  .card--front { top: 190px; }
  .card--back { top: 640px; }

  .brand {
    position: absolute; left: 0; width: 100%;
    display: flex; align-items: center; justify-content: center; gap: 10px;
    font-family: var(--sans); font-weight: 500; color: var(--ink);
  }
  .brand__dot {
    width: 12px; height: 12px; border-radius: 50%; background: var(--wine);
  }
  .card--front .brand { top: 92px; font-size: 22px; }

  .tagline-rule {
    position: absolute; left: 104px; width: 412px; height: 1px; background: var(--ink);
  }
  .tagline-rule--top { top: 178px; }
  .tagline-rule--bottom { top: 237px; }
  .tagline {
    position: absolute; top: 182px; left: 0; width: 100%;
    text-align: center;
    font-family: var(--script); font-size: 35px; color: var(--wine);
    word-spacing: 4px;
  }
  .subline {
    position: absolute; top: 246px; left: 0; width: 100%;
    text-align: center;
    font-family: var(--sans); font-weight: 400; font-size: 19px; color: var(--ink);
    letter-spacing: .5px;
  }
  .front-footer { position: absolute; left: 0; bottom: 0; width: 620px; height: 50px; }
  .front-footer__url {
    position: absolute; left: 0; bottom: 12px; width: 100%;
    text-align: center;
    font-family: var(--sans); font-weight: 700; font-size: 16px;
    color: var(--white); letter-spacing: 2.5px;
  }

  .name-plate { position: absolute; right: 0; top: 20px; width: 360px; height: 77px; }
  .name-plate__title {
    position: absolute; left: 302px; top: 26px;
    font-family: var(--script); font-size: 26px; color: var(--white); white-space: nowrap;
  }
  .name-plate__line {
    position: absolute; left: 302px; top: 66px;
    font-family: var(--sans); font-size: 12.5px; color: var(--white); white-space: nowrap;
  }
  .card--back .brand { top: 164px; width: 262px; font-size: 16px; }

  .contacts { position: absolute; left: 293px; top: 121px; width: 300px; height: 176px; }
  .contact {
    position: absolute; left: 43px;
    font-family: var(--sans); font-weight: 700; font-size: 15px; color: var(--ink);
    white-space: nowrap; transform: translateY(-50%);
  }
  .back-wave { position: absolute; left: 0; bottom: 0; width: 620px; height: 50px; }
</style>
</head>
<body>

<section class="card card--front">
  <div class="brand"><span class="brand__dot"></span>Hotel Lindenwäldchen</div>
  <div class="tagline-rule tagline-rule--top"></div>
  <p class="tagline">Entspannen Loslassen Auftanken</p>
  <div class="tagline-rule tagline-rule--bottom"></div>
  <p class="subline">Urlaub an einem besonderen Ort</p>
  <svg class="front-footer" viewBox="0 0 620 50">
    <rect x="0" y="34" width="620" height="16" fill="var(--wine)"/>
    <path d="M118 50 L134 7 Q136 1 143 1 L481 1 Q488 1 491 7 L505 50 Z" fill="var(--black)"/>
  </svg>
  <p class="front-footer__url">www.lindenwaeldchen.net</p>
</section>

<section class="card card--back">
  <svg class="name-plate" viewBox="0 0 360 77">
    <path d="M0 0 L360 0 L360 77 L38 77 Q30 77 26 70 Z" fill="var(--wine)"/>
  </svg>
  <p class="name-plate__title" style="left:302px">Marta &amp; das Lindenwäldchen</p>
  <p class="name-plate__line">Marta Brecke - Grauer Pfad 7</p>

  <div class="brand"><span class="brand__dot"></span>Hotel Lindenwäldchen</div>

  <div class="contacts">
    <svg width="40" height="176" viewBox="0 0 40 176" style="position:absolute;left:0;top:0">
      <line x1="16" y1="16" x2="16" y2="160" stroke="var(--wine)" stroke-width="2"/>
      <g fill="var(--paper-light)" stroke="var(--wine)" stroke-width="2">
        <circle cx="16" cy="16" r="15"/>
        <circle cx="16" cy="64" r="15"/>
        <circle cx="16" cy="113" r="15"/>
        <circle cx="16" cy="160" r="15"/>
      </g>
      <!-- phone -->
      <path d="M11 10 q-2 2 0 6 q3 5 7 6 q3 1 4-1 l-2-2 q-1-1-2 0 q-3-1-4-4 q1-1 0-2 z" fill="var(--wine)"/>
      <!-- envelope -->
      <rect x="9" y="59" width="14" height="10" rx="1" fill="var(--wine)"/>
      <path d="M9 60 L16 65 L23 60" fill="none" stroke="var(--paper-light)" stroke-width="1.2"/>
      <!-- pin -->
      <path d="M16 122 C11 116 10 113 10 110 a6 6 0 0 1 12 0 c0 3-1 6-6 12 z" fill="var(--wine)"/>
      <circle cx="16" cy="110" r="2.2" fill="var(--paper-light)"/>
      <!-- globe -->
      <g fill="none" stroke="var(--wine)" stroke-width="1.4">
        <circle cx="16" cy="160" r="7"/>
        <ellipse cx="16" cy="160" rx="3" ry="7"/>
        <line x1="9" y1="160" x2="23" y2="160"/>
      </g>
    </svg>
    <p class="contact" style="top:16px">43 (5817) 40926</p>
    <p class="contact" style="top:64px">post@marta-brecke.de</p>
    <p class="contact" style="top:113px">18471 Alt Feldow</p>
    <p class="contact" style="top:160px">www.lindenwaeldchen.net</p>
  </div>

  <svg class="back-wave" viewBox="0 0 620 50" preserveAspectRatio="none">
    <path d="M0 35 C20 10 60 0 110 8 C160 16 190 30 240 28 C290 26 300 12 340 12 C380 12 400 30 450 28 C500 26 520 10 560 14 C590 17 605 22 620 22 L620 50 L0 50 Z" fill="var(--wine)"/>
  </svg>
</section>

</body>
</html>
```